Faris Methani Business Card

I would like an elegant business card design in both english and arabic.

Ideally a logo design with my name in Arabic (could be a tiger for example)

It should have my Name : Faris Methani
Title: Advisor / Investor
Tel. UAE +971 558 274 903
UK +44 7821 560 287
Email. farmethani412@mailvane.net

I am an active angle investor and have many business interests in the TMT space and invest globally, the design needs to be fresh, elegant and striking.

The design should be catching and grab one's attention when they view the card.

Front card should be in English and Reverse in Arabic....

Target Market(s)

Global Investors, CEO's

Industry/Entity Type

Business

Contact Information for Business Card

Title: Advisor / Investor
Tel. UAE +971 558 274 903
UK +44 7821 560 287

Font styles to use
Serif
Other font styles liked:
• Palantino

Requirements
Must have
• A striking design with a play of my name in Arabic, could be my name that is designed as a tiger for example

```html
<!DOCTYPE html>
<html lang="en">
<head>
<meta charset="UTF-8">
<title>Faris Methani Business Card</title>
<link rel="stylesheet" href="https://fonts.googleapis.com/css2?family=Cinzel:wght@400&family=Open+Sans:wght@400&display=swap">
<style>
  :root {
    --paper: #ffffff;
    --card: #000000;
    --ink: #ffffff;
    --art-light: #e6e6e6;
    --art-mid: #7a7a7a;
    --art-fade: #000000;
  }
  * { margin: 0; padding: 0; box-sizing: border-box; }
  html, body {
    width: 1200px;
    height: 397px;
    overflow: hidden;
    background: var(--paper);
  }
  .sheet {
    position: relative;
    width: 1200px;
    height: 397px;
    background: var(--paper);
  }
  .card {
    position: absolute;
    top: 18px;
    height: 358px;
    background: var(--card);
    color: var(--ink);
    overflow: hidden;
  }
  .card--front { left: 18px; width: 585px; }
  .card--back { left: 628px; width: 554px; }

  .identity__name {
    position: absolute;
    left: 50px;
    top: 140px;
    font-family: "Cinzel", "Palatino Linotype", serif;
    font-size: 48px;
    font-weight: 400;
    letter-spacing: 0.5px;
    line-height: 1;
    white-space: nowrap;
  }
  .identity__title {
    position: absolute;
    left: 206px;
    top: 200px;
    font-family: "Cinzel", "Palatino Linotype", serif;
    font-size: 18px;
    font-weight: 400;
    letter-spacing: 0.5px;
    line-height: 1;
    white-space: nowrap;
  }
  .identity__mark {
    position: absolute;
    left: 424px;
    top: 126px;
    width: 86px;
    height: 72px;
  }
  .contact {
    position: absolute;
    font-family: "Open Sans", Arial, sans-serif;
    font-style: normal;
    font-weight: 400;
    font-size: 19px;
    line-height: 25px;
    white-space: nowrap;
  }
  .contact--phones {
    right: 56px;
    top: 290px;
    text-align: right;
  }
  .contact--email {
    right: 28px;
    top: 312px;
  }
  .tiger-art {
    position: absolute;
    left: 30px;
    top: 20px;
    width: 300px;
    height: 285px;
  }
</style>
</head>
<body>
<main class="sheet">
  <section class="card card--front" aria-label="Front of card">
    <h1 class="identity__name">Faris Methani</h1>
    <p class="identity__title">Advisor / Investor</p>
    <svg class="identity__mark" viewBox="0 0 86 72" role="img" aria-label="Small tiger head illustration in white on black">
      <defs>
        <radialGradient id="markTone" cx="50%" cy="50%" r="50%">
          <stop offset="0%" stop-color="var(--art-light)"/>
          <stop offset="55%" stop-color="var(--art-mid)"/>
          <stop offset="100%" stop-color="var(--art-fade)"/>
        </radialGradient>
      </defs>
      <ellipse cx="43" cy="36" rx="43" ry="36" fill="url(#markTone)"/>
    </svg>
    <address class="contact contact--phones">
      UAE + 971 558 274 903<br>
      UK + 44 7821 560 287
    </address>
  </section>

  <section class="card card--back" aria-label="Back of card">
    <svg class="tiger-art" viewBox="0 0 300 285" role="img" aria-label="Large roaring tiger head illustration in white on black, facing right">
      <defs>
        <radialGradient id="tigerTone" cx="50%" cy="50%" r="50%">
          <stop offset="0%" stop-color="var(--art-light)"/>
          <stop offset="50%" stop-color="var(--art-mid)"/>
          <stop offset="100%" stop-color="var(--art-fade)"/>
        </radialGradient>
      </defs>
      <ellipse cx="150" cy="142" rx="150" ry="142" fill="url(#tigerTone)"/>
    </svg>
    <address class="contact contact--email">farmethani412@mailvane.net</address>
  </section>
</main>
</body>
</html>
```